WORDPRESS DESIGN - PROFESSIONAL SERVICES

Objective:
Design a new Wordpress e-commerce website for www.rolvekcareers.com.au .

Rolvek Careers provides professional CV/resume writing services for Australian IT professionals. This assignment is to upgrade an existing 25 page e-commerce website - www.rolvekcareers.com.au

Process:
The contract is to design of the website. ArtHarbor designers need to submit a home page design based on the attached files and wireframes. RLVK will judge these submissions and the winner will be awarded $350 to design the 25 page website for Wordpress

Design:
You will be given Pennlow Wireframes, images and copy to base your design on. You can choose any font or colour palette, although it is preferred if you base it on the existing logo.

The design must be:
• Corporate
• Compelling
• Trustworthy

Development:
Development will be a separate assignment. The existing website to be upgraded is built on WordPress and Cartivo.

You will be provided:
a) Logo
b) Suggested Colour palette
c) 25 Pennlow Wireframes
d) Images
e) Copy

Process:
1) Submit home page designs based on Home ATF and Home BTF.
2) Winner gets $350 design contract
3) Design sign-off
4) Payment

Target Market(s)

Customer Profile:

• Professional
• IT Professionals
• Earn $100k+
• Corporate
• University/Tertiary Educatation
• 80% men
• Live in Australian cities
• Mix of European, Indian and Asian backgrounds
• 75% are 30-50 y/o

Industry/Entity Type

E-Commerce

Font styles to use
Sans Serif

Colors
0355a3
3176b5
85abd2

Requirements
Must have
• The design must be:
• Corporate
• Compelling
• Trustworthy

* Lay-out should be based on the wireframes provided by RLVK
* The top banner is very important and will be on every page.
* There are a lot of words on the page so one of the challenges is to make it not look crowded and busy.
* It needs to look modern and professional. Use some creativity.
* The three key buttons we want users to click is the 'Click Me' next to products and the 'Shop' icon. Please highlight these (maybe in a different colour or with a frame)
* The font is very important.
Nice to have
• The font and colour palette you choose matches the existing logo

```html
<!DOCTYPE html>
<html lang="en">
<head>
<meta charset="utf-8">
<title>Rolvek Careers – CV Writing for IT Professionals</title>
<link rel="stylesheet" href="https://fonts.googleapis.com/css2?family=Open+Sans:wght@400;600;700&family=Noto+Serif:wght@700&family=Oswald:wght@500&display=swap">
<style>
:root{
  --brand-dark:#0355a3;
  --brand-mid:#3176b5;
  --brand-light:#85abd2;
  --navy:#1c3f73;
  --text:#444;
  --muted:#888;
  --panel:#ececec;
  --button-grey:#d6d6d6;
  --tick:#2f9a3a;
  --seal:#e3b23c;
  --footer:#46484b;
  --footer-panel:#3a3b3d;
  --field:#6e7073;
  --white:#fff;
}
*{box-sizing:border-box;margin:0;padding:0}
html,body{width:1200px;height:1094px;overflow:hidden;background:var(--white)}
body{position:relative;font-family:"Open Sans",Arial,sans-serif;color:var(--text);font-size:8.5px}
h1,h2,h3{font-weight:400}
.abs{position:absolute}

/* top banner */
.top-banner{left:0;top:0;width:1200px;height:37px;background:var(--brand-light);border-top:3px solid var(--brand-dark);border-bottom:1px solid var(--brand-mid)}
.main-nav a{position:absolute;top:13px;color:var(--white);font-size:8.5px;text-decoration:none}
.main-nav a.is-active{color:var(--brand-dark)}
.main-nav a.is-active::after{content:"";position:absolute;left:0;right:0;bottom:-3px;height:1px;background:var(--brand-dark)}
.cart-tab{left:678px;top:0;width:112px;height:37px;background:var(--brand-dark);border-radius:0 0 6px 12px;color:var(--white);font-size:6px;line-height:9px}
.cart-tab svg{position:absolute;left:8px;top:10px}
.cart-tab .cart-text{position:absolute;left:37px;top:10px;letter-spacing:.2px}

/* intro */
.brand-mark{left:328px;top:63px;width:55px;height:55px;border-radius:50%;background:var(--brand-mid);border:3px solid var(--brand-light);color:var(--white);font-weight:700;font-size:13px;display:flex;align-items:center;justify-content:center}
.page-title{left:401px;top:69px;font-family:"Noto Serif",Georgia,serif;font-weight:700;font-size:14px;color:var(--navy)}
.page-lede{left:401px;top:91px;width:390px;font-size:7px;line-height:11px;color:#333}

.hero{left:326px;top:143px;width:457px;height:201px;background:linear-gradient(90deg,#e8eef4 0%,#c7d0da 40%,#dfe5ea 65%,#f2f2f2 100%);border:1px solid #e3e3e3}
.hero-portrait{left:618px;top:143px;width:165px;height:201px;background:linear-gradient(180deg,#7a4a32 0%,#c99b7d 40%,#b9bec6 75%,#9aa2ad 100%)}
.hero-points{left:342px;top:236px;list-style:none;font-size:9.5px;color:#222}
.hero-points li{height:23px;display:flex;align-items:center;gap:8px}

/* process */
.section-heading{font-size:10px;color:var(--brand-dark)}
.process-heading{left:328px;top:375px}
.process-list{left:327px;top:411px;list-style:none;font-size:7.5px;color:#333}
.process-list li{height:21.2px;display:flex;align-items:center;gap:10px}
.guarantee-arc{left:629px;top:403px}

/* client's speaks */
.divider-heading{left:326px;top:557px;width:459px;height:16px}
.divider-heading::before{content:"";position:absolute;left:0;right:0;top:8px;height:2px;background:#e2e2e2}
.divider-heading span{position:absolute;left:185px;top:0;padding:0 14px;background:var(--white);font-family:"Oswald",Arial,sans-serif;font-weight:500;font-size:9.5px;color:#444}
.client-photo{left:326px;top:616px;width:136px;height:84px;background:linear-gradient(135deg,#c4c7cc 0%,#8d9299 55%,#3a3c40 100%)}
.client-title{left:473px;top:613px;font-size:9.5px;color:#555}
.client-text{left:473px;top:636px;width:312px;font-size:7px;line-height:11px;color:#777}
.client-byline{left:476px;top:690px;font-size:7.5px;color:#555}
.client-byline b{color:var(--navy)}
.client-byline small{color:var(--muted);font-size:6.5px}
.share-bar{left:326px;top:711px;width:459px;height:25px;border-top:1px solid #ddd;border-bottom:1px solid #ddd}
.share-btn{position:absolute;top:6px;height:12px;font-size:6px;font-weight:700;color:var(--white);display:flex;align-items:center;justify-content:center;border-radius:1px}
.pager{position:absolute;top:5px;width:13px;height:13px;border-radius:50%;background:#ccc;display:flex;align-items:center;justify-content:center}

/* sidebar */
.track-box{left:796px;top:62px;width:171px;height:162px;background:var(--panel)}
.track-title{left:808px;top:83px;font-size:7.5px;font-weight:600;color:#333}
.guarantee-seal{left:814px;top:111px;width:42px;height:42px;border-radius:50%;background:var(--seal)}
.track-list{left:873px;top:110px;font-size:7px;line-height:10.8px;color:#555}
.track-list b{color:#444}
.track-call{left:796px;top:184px;width:171px;height:40px;background:var(--brand-light);color:var(--white);font-size:7.5px;font-weight:700;text-align:center;padding-top:9px;line-height:11px}
.social-row{left:796px;width:171px;height:29px;background:var(--button-grey);border-radius:4px;font-size:6.5px;color:#555;padding:0 0 0 17px;display:flex;align-items:center}
.social-row i{position:absolute;right:4px;top:1px;width:27px;height:27px;border-radius:50%;background:#ebebeb}
.testimonials-head{left:797px;top:356px;width:170px;font-size:10px;color:var(--brand-dark)}
.testimonials-head small{position:absolute;right:0;top:2px;font-size:7px;color:var(--muted)}
.testimonial-card{left:796px;top:379px;width:171px;height:160px;background:#f0f0f0}
.testimonial-avatar{left:846px;top:393px;width:65px;height:65px;border-radius:50%;border:3px solid var(--tick);background:linear-gradient(180deg,#4a2f22,#c09a80)}
.testimonial-name{left:796px;top:464px;width:171px;text-align:center;font-size:8px;color:#444}
.testimonial-role{left:796px;top:476px;width:171px;text-align:center;font-size:7px;font-style:italic;color:var(--brand-dark)}
.testimonial-quote{left:810px;top:492px;width:150px;font-size:6.3px;line-height:11px;color:#666}
.newsletter-copy{left:797px;top:580px;width:175px;font-size:7.5px;line-height:11px;color:var(--brand-dark)}
.newsletter-input{left:796px;top:615px;width:171px;height:27px;background:#f5f5f5;border:1px solid #e6e6e6;font-size:7px;color:#aaa;display:flex;align-items:center;padding-left:31px}
.newsletter-input svg{position:absolute;left:9px;top:9px}

/* footer */
.site-footer{left:0;top:770px;width:1200px;height:324px;background:var(--footer);border-top:2px solid var(--brand-light)}
.footer-brand-panel{left:326px;top:772px;width:201px;height:284px;background:var(--footer-panel)}
.footer-logo{left:392px;top:801px;width:55px;height:55px;border-radius:50%;background:var(--footer-panel);border:3px solid #9b9b9b;color:#ddd;font-size:12px;font-weight:700;display:flex;align-items:center;justify-content:center}
.footer-rule{left:348px;top:875px;width:155px;height:1px;background:#5a5b5d}
.footer-social{left:385px;top:893px;display:flex;gap:3px}
.footer-social i{width:17px;height:17px;border-radius:50%;background:#b8b8b8}
.footer-social i:first-child{background:var(--brand-mid)}
.footer-heading{font-size:11.5px;color:#e6e6e6;letter-spacing:.3px}
.contact-item{left:590px;font-size:7.5px;line-height:11px;color:#bbb}
.contact-item svg{position:absolute;left:0;top:1px}
.contact-item div{margin-left:23px}
.contact-item b{color:#ccc}
.form-field{left:815px;width:152px;height:24px;background:var(--field);border:1px solid #8a8c8f;font-size:7.5px;color:#ddd;padding:7px 7px}
.form-field i{position:absolute;right:2px;top:2px;width:19px;height:18px;background:#56585b}
.send-btn{left:815px;top:1017px;width:66px;height:24px;background:linear-gradient(180deg,#4d90d4,var(--brand-dark));color:var(--white);font-family:"Oswald",Arial,sans-serif;font-weight:500;font-size:10px;display:flex;align-items:center;padding-left:16px;gap:11px}
.footer-bottom-rule{left:33px;top:1056px;width:1167px;height:1px;background:#56585b}
.copyright{left:327px;top:1072px;font-size:6.5px;color:#888}
</style>
</head>
<body>

<header class="abs top-banner">
  <nav class="main-nav">
    <a class="is-active" style="left:327px" href="#">Home</a>
    <a style="left:375px" href="#">Shop</a>
    <a style="left:423px" href="#">Map</a>
    <a style="left:466px" href="#">Testimonials</a>
    <a style="left:536px" href="#">About us</a>
    <a style="left:596px" href="#">Contact Us</a>
  </nav>
</header>
<div class="abs cart-tab">
  <svg width="22" height="16" viewBox="0 0 22 16"><path d="M1 2h4l3 9h10l3-7H7" fill="none" stroke="#fff" stroke-width="1.6"/><circle cx="9" cy="14" r="1.6" fill="#fff"/><circle cx="17" cy="14" r="1.6" fill="#fff"/></svg>
  <div class="cart-text">SHOPPING CART<br>ITEMS 0 - <b>$0.00</b></div>
</div>

<main>
  <div class="abs brand-mark">RLVK</div>
  <h1 class="abs page-title">CV Writing for IT Professionals</h1>
  <p class="abs page-lede">We deliver IT especialist CV's and ProLink profiles that showcase your value and acheve high search ranking in ProLink and recruitment database</p>

  <div class="abs hero" role="img" aria-label="Blurred office team in the background"></div>
  <div class="abs hero-portrait" role="img" aria-label="Smiling businesswoman in a grey blazer"></div>
  <ul class="abs hero-points">
    <li><svg width="10" height="8" viewBox="0 0 10 8"><path d="M1 4l3 3 5-6" fill="none" stroke="#1c3f73" stroke-width="1.4"/></svg>Make sure employers find and like your CV</li>
    <li><svg width="10" height="8" viewBox="0 0 10 8"><path d="M1 4l3 3 5-6" fill="none" stroke="#1c3f73" stroke-width="1.4"/></svg>Get a CV that is high impact, IT specialised and search optimised.</li>
    <li><svg width="10" height="8" viewBox="0 0 10 8"><path d="M1 4l3 3 5-6" fill="none" stroke="#1c3f73" stroke-width="1.4"/></svg>RLVK offers a 100% Satisfaction Guarantee</li>
  </ul>

  <h2 class="abs section-heading process-heading">How we will write your CV and ProLink Profile:</h2>
  <ul class="abs process-list">
    <li><svg width="9" height="7" viewBox="0 0 10 8"><path d="M1 4l3 3 5-6" fill="none" stroke="#2f9a3a" stroke-width="1.5"/></svg>We start with your career aspiration and most recent CV.</li>
    <li><svg width="9" height="7" viewBox="0 0 10 8"><path d="M1 4l3 3 5-6" fill="none" stroke="#2f9a3a" stroke-width="1.5"/></svg>We ask questions by email to fill in any missing information.</li>
    <li><svg width="9" height="7" viewBox="0 0 10 8"><path d="M1 4l3 3 5-6" fill="none" stroke="#2f9a3a" stroke-width="1.5"/></svg>We produce 3-4 drafts before delivering the final version.</li>
    <li><svg width="9" height="7" viewBox="0 0 10 8"><path d="M1 4l3 3 5-6" fill="none" stroke="#2f9a3a" stroke-width="1.5"/></svg>When you're happy with the results, you approved the new CV.</li>
    <li><svg width="9" height="7" viewBox="0 0 10 8"><path d="M1 4l3 3 5-6" fill="none" stroke="#2f9a3a" stroke-width="1.5"/></svg>You then get a search optimised ProLink profile based on your new CV.</li>
    <li><svg width="9" height="7" viewBox="0 0 10 8"><path d="M1 4l3 3 5-6" fill="none" stroke="#2f9a3a" stroke-width="1.5"/></svg>We work however fast or slow you want us to.</li>
  </ul>
  <svg class="abs guarantee-arc" width="155" height="98" viewBox="0 0 155 98">
    <defs><path id="arc" d="M12 72 A66 60 0 0 1 143 72"/></defs>
    <text font-family="Open Sans, Arial, sans-serif" font-size="12" fill="#2f9a3a"><textPath href="#arc" startOffset="50%" text-anchor="middle">30 Days Money Back Gurantee</textPath></text>
    <circle cx="77" cy="62" r="28" fill="#e3b23c"/>
  </svg>

  <div class="abs divider-heading"><span>CLIENT'S SPEAKS</span></div>
  <div class="abs client-photo" role="img" aria-label="Client seated on office stairs"></div>
  <h3 class="abs client-title">Lorem Ipsum is simply dummy text of the printing</h3>
  <p class="abs client-text">Lorem Ipsum is simply dummy text of the printing and typesetting industry. Lorem Ipsum has been the industry's standard dummy text ever since the 1500s, when an unknown printer took a galley of type and scrambled it to make a type specimen book</p>
  <p class="abs client-byline">Bexley Technology, <b>Bexley</b> &nbsp;- &nbsp;<small>24 July 2014</small></p>
  <div class="abs share-bar">
    <span class="share-btn" style="left:9px;width:27px;background:#1da1e0">Share</span>
    <span class="share-btn" style="left:46px;width:27px;background:#3b5998">Like</span>
    <span class="share-btn" style="left:82px;width:27px;background:#555">+1</span>
    <span class="pager" style="left:428px"><svg width="5" height="7" viewBox="0 0 5 7"><path d="M4 0.5L1 3.5 4 6.5" fill="none" stroke="#666"/></svg></span>
    <span class="pager" style="left:445px"><svg width="5" height="7" viewBox="0 0 5 7"><path d="M1 0.5L4 3.5 1 6.5" fill="none" stroke="#666"/></svg></span>
  </div>
</main>

<aside>
  <div class="abs track-box"></div>
  <h3 class="abs track-title">IT Specialist CV's &amp; ProLink Profiles</h3>
  <div class="abs guarantee-seal"></div>
  <div class="abs track-list"><b>Proven track record:</b><br><br>300 IT Placements<br>100% Client Satisfaction<br>20,000 IT CV's Reviewed<br>7 Years in IT Recruitment</div>
  <div class="abs track-call">Call Mark on +613 9555 0142<br>Email: info@rolvekcareers.com.au</div>

  <div class="abs social-row" style="top:255px">Connect with me on ProLink<i></i></div>
  <div class="abs social-row" style="top:291px">Follow me on CircleNet<i></i></div>

  <h2 class="abs testimonials-head">TESTIMONIALS<small>view all +</small></h2>
  <div class="abs testimonial-card"></div>
  <div class="abs testimonial-avatar" role="img" aria-label="Portrait of the reviewer"></div>
  <p class="abs testimonial-name">Bexley Technology</p>
  <p class="abs testimonial-role">Web Developer</p>
  <p class="abs testimonial-quote">Lorem Ipsum is simply dummy text of the printing and typesetting industry. Lorem Ipsum has been the industry's standard dummy</p>

  <p class="abs newsletter-copy">Register easily for our free recruitment coaching newsletter and special offers:</p>
  <div class="abs newsletter-input"><svg width="14" height="10" viewBox="0 0 14 10"><rect width="14" height="10" fill="#bbb"/><path d="M0 0l7 5 7-5" fill="none" stroke="#f5f5f5"/></svg>your email</div>
</aside>

<footer>
  <div class="abs site-footer"></div>
  <div class="abs footer-brand-panel"></div>
  <div class="abs footer-logo">RLVK</div>
  <div class="abs footer-rule"></div>
  <div class="abs footer-social"><i></i><i></i><i></i><i></i></div>

  <h3 class="abs footer-heading" style="left:590px;top:803px">CONTACTS</h3>
  <div class="abs contact-item" style="top:830px">
    <svg width="13" height="13" viewBox="0 0 13 13"><path d="M6.5 1L0.5 6.5h2V12h3V8.5h2V12h3V6.5h2z" fill="#bbb"/></svg>
    <div><b>Company Name</b><br># Street Name, 237<br>City Name, Country, 1234<br>T: (11) 2222- 333333</div>
  </div>
  <div class="abs contact-item" style="top:889px">
    <svg width="12" height="13" viewBox="0 0 12 13"><path d="M2 1l3 0 1 3-2 1.5c1 2 2 3 3.5 4L9 7.5l3 1v3c-6 1-11-5-10-10.5z" fill="#bbb"/></svg>
    <div>Phone: (11) 22222- 33333<br>Fax: (123) 123 45678 00</div>
  </div>
  <div class="abs contact-item" style="top:930px">
    <svg width="13" height="10" viewBox="0 0 13 10"><rect width="13" height="10" fill="#bbb"/><path d="M0 0l6.5 5 6.5-5" fill="none" stroke="#46484b"/></svg>
    <div>contato@example.com</div>
  </div>

  <h3 class="abs footer-heading" style="left:814px;top:803px">GET IN TOUCH</h3>
  <div class="abs form-field" style="top:831px">Name<i></i></div>
  <div class="abs form-field" style="top:859px">Telephone<i></i></div>
  <div class="abs form-field" style="top:888px">Email<i></i></div>
  <div class="abs form-field" style="top:917px;height:88px">Message<i></i></div>
  <div class="abs send-btn">SEND <svg width="13" height="9" viewBox="0 0 13 9"><path d="M1 4.5l3.5 3.5L12 1" fill="none" stroke="#fff" stroke-width="1.6"/></svg></div>

  <div class="abs footer-bottom-rule"></div>
  <p class="abs copyright">Copyright © 2014 Company Name.</p>
</footer>

</body>
</html>
```